Name Card, Stationary, Warranty Seal, Receipt Book
Qorvix Repair Centre
Simple
Tomas
27 Wexley Lane #08-04
Singapore 58817
qrv@qorvix-mail.test
www.qorvix-fix.test
State in we Repair veltra, Plumstone, Korvane and others Smart Phones
On the spot Repair.
For this you are able to use your creative base on our line of repair service

```html
<!DOCTYPE html>
<html lang="en">
<head>
<meta charset="utf-8">
<title>Qorvix Repair Centre — Name Card</title>
<link rel="stylesheet" href="https://fonts.googleapis.com/css2?family=Open+Sans:wght@400;600;700;800&display=swap">
<style>
  :root {
    --backdrop: #e9e6e1;
    --card: #ffffff;
    --brand-blue: #1f4fa6;
    --brand-orange: #f2701f;
    --brand-red: #e2381d;
    --brand-yellow: #f7a427;
    --text-dark: #3a3a3a;
    --rule: #c9c9c9;
  }
  * { box-sizing: border-box; margin: 0; padding: 0; }
  html, body {
    width: 1200px;
    height: 780px;
    overflow: hidden;
    background: var(--backdrop);
    font-family: "Open Sans", Arial, sans-serif;
  }
  .canvas {
    width: 1200px;
    height: 780px;
    display: flex;
    align-items: center;
    justify-content: center;
  }
  .name-card {
    position: relative;
    width: 1000px;
    height: 600px;
    background: var(--card);
    border-radius: 30px;
    overflow: hidden;
    box-shadow: 0 10px 30px rgba(0,0,0,0.18);
  }
  .brand {
    position: absolute;
    top: 86px;
    left: 0;
    width: 100%;
    display: flex;
    align-items: center;
    justify-content: center;
    gap: 22px;
  }
  .brand-dot {
    width: 86px;
    height: 86px;
    border-radius: 50%;
    background: var(--brand-blue);
  }
  .brand-name {
    color: var(--brand-orange);
    font-weight: 800;
    line-height: 1;
  }
  .brand-name .primary {
    display: block;
    font-size: 80px;
    letter-spacing: 1px;
    text-transform: uppercase;
  }
  .brand-name .secondary {
    display: block;
    font-size: 27px;
    letter-spacing: 3px;
    text-transform: uppercase;
    margin-top: 4px;
    text-align: right;
  }
  .holder {
    position: absolute;
    top: 276px;
    right: 530px;
    text-align: right;
    color: var(--text-dark);
  }
  .holder-name {
    color: var(--brand-blue);
    font-weight: 700;
    font-size: 30px;
    margin-bottom: 22px;
  }
  .holder-address {
    font-size: 20px;
    line-height: 1.35;
  }
  .divider {
    position: absolute;
    top: 270px;
    left: 500px;
    width: 2px;
    height: 130px;
    background: var(--rule);
  }
  .contacts {
    position: absolute;
    top: 268px;
    left: 526px;
    list-style: none;
    color: var(--text-dark);
    font-size: 20px;
  }
  .contacts li {
    display: flex;
    align-items: center;
    gap: 14px;
    height: 35px;
  }
  .contacts svg {
    width: 20px;
    height: 20px;
    fill: var(--brand-blue);
    flex: none;
  }
  .footer-band {
    position: absolute;
    left: 0;
    bottom: 0;
    width: 100%;
    height: 110px;
    background: linear-gradient(90deg, var(--brand-blue) 0%, var(--brand-red) 45%, var(--brand-orange) 70%, var(--brand-yellow) 100%);
  }
</style>
</head>
<body>
<main class="canvas">
  <section class="name-card">
    <header class="brand">
      <span class="brand-dot"></span>
      <span class="brand-name">
        <span class="primary">Qorvix</span>
        <span class="secondary">Repair Centre</span>
      </span>
    </header>

    <div class="holder">
      <p class="holder-name">Tomas</p>
      <p class="holder-address">27 Wexley Lane #08-04<br>Singapore 58817</p>
    </div>

    <div class="divider"></div>

    <ul class="contacts">
      <li>
        <svg viewBox="0 0 24 24" aria-hidden="true"><path d="M6.6 10.8a15.1 15.1 0 0 0 6.6 6.6l2.2-2.2c.3-.3.7-.4 1-.2 1.1.4 2.3.6 3.6.6.6 0 1 .4 1 1V20c0 .6-.4 1-1 1A17 17 0 0 1 3 4c0-.6.4-1 1-1h3.5c.6 0 1 .4 1 1 0 1.3.2 2.5.6 3.6.1.3 0 .7-.2 1z"/></svg>
        <span>90017264</span>
      </li>
      <li>
        <svg viewBox="0 0 24 24" aria-hidden="true"><path d="M7 2h10v6H7zM4 9h16a2 2 0 0 1 2 2v6h-4v5H6v-5H2v-6a2 2 0 0 1 2-2zm4 8v3h8v-3z"/></svg>
        <span>61005520</span>
      </li>
      <li>
        <svg viewBox="0 0 24 24" aria-hidden="true"><path d="M12 2a10 10 0 1 0 5 18.7l-1-1.7A8 8 0 1 1 20 12v1.2a1.8 1.8 0 0 1-3.6 0V7h-2v1a5 5 0 1 0 .7 7.2A3.8 3.8 0 0 0 22 13.2V12A10 10 0 0 0 12 2zm0 13a3 3 0 1 1 0-6 3 3 0 0 1 0 6z"/></svg>
        <span>qrv@qorvix-mail.test</span>
      </li>
      <li>
        <svg viewBox="0 0 24 24" aria-hidden="true"><path d="M12 2a10 10 0 1 0 0 20 10 10 0 0 0 0-20zm6.9 9h-3a15 15 0 0 0-1.3-6A8 8 0 0 1 18.9 11zM12 4c.9 1.3 1.7 3.8 1.9 7h-3.8C10.3 7.8 11.1 5.3 12 4zM9.4 5a15 15 0 0 0-1.3 6h-3A8 8 0 0 1 9.4 5zM5.1 13h3a15 15 0 0 0 1.3 6A8 8 0 0 1 5.1 13zM12 20c-.9-1.3-1.7-3.8-1.9-7h3.8c-.2 3.2-1 5.7-1.9 7zm2.6-1a15 15 0 0 0 1.3-6h3a8 8 0 0 1-4.3 6z"/></svg>
        <span>www.qorvix-fix.test</span>
      </li>
    </ul>

    <div class="footer-band" role="img" aria-label="Decorative blue and orange wave along the bottom edge of the card"></div>
  </section>
</main>
</body>
</html>
```